automatic Real Estate Sales Brochure

Print-out of 3 to 8 pages automatically on a color inkjet printer. Page size A4
All details for my Real Estate Sales Design Project are in attached file.
Here some points:
We have abound 100 real estate objects for sale (houses, flats and pieces of land).
For each item, our system creates automatically a sales documentation, which we print out and hand to the potential buyers after they've visited the object or send it by mail upon request in form of a pdf.
This document should be of 3 to maximum 8 pages.
It should be of a modern design and invite the client to read it.
The information should be clear and quick to find.
If the global look could somehow relate to the look of our web site www.velorancasa.ch, that would be nice.
The company data is there for legal reasons, but it is the agent's phone and mail that the clients should use for contact.
The photos should be of big size (2 by page?) without being distorted nor cut.
Optionally, to save ink and pages, maybe only the first 3-4 photos full size and the rest smaller?

Target Market(s)

will be printed or sent as PDF "on the fly", meaning no pre-printing at a print shop!

Industry/Entity Type

Real Estate

Font styles to use
Sans Serif

Requirements
Must have
• see details in attached file
Should not have
• no edge-to-edge printing
• no double-page printing (A3)

```html
<!DOCTYPE html>
<html lang="fr">
<head>
<meta charset="utf-8">
<title>Veloran Casa – Fiche de vente</title>
<link href="https://fonts.googleapis.com/css2?family=Roboto+Condensed:wght@300;400;700&display=swap" rel="stylesheet">
<style>
  :root{
    --backdrop:#939598;
    --red:#ef4a35;
    --red-line:#d9634f;
    --ink:#1a1a1a;
    --panel-grey:#c9c9ca;
    --divider:#58595b;
    --footer-dark:#0d0d0d;
    --footer-grey:#58595b;
    --white:#ffffff;
  }
  *{box-sizing:border-box;margin:0;padding:0}
  html,body{width:889px;height:1200px;overflow:hidden}
  body{background:var(--backdrop);font-family:"Roboto Condensed",sans-serif;color:var(--ink);position:relative}
  .sheet{position:absolute;left:56px;top:51px;width:776px;height:1097px;background:var(--white);overflow:hidden}

  .hero{position:absolute;left:0;top:0;width:776px;height:581px}
  .hero-photo{position:absolute;inset:0;background:linear-gradient(180deg,#e9e7e8 0%,#e2ddd8 45%,#b07a45 62%,#8a5a2d 100%)}
  .hero-accent{position:absolute;inset:0}
  .brand{position:absolute;left:28px;top:32px;font-weight:700;font-size:54px;line-height:1;color:var(--red);letter-spacing:-1px}
  .tagline{position:absolute;left:28px;top:110px;font-weight:700;font-size:21px;color:var(--white)}
  .headline{position:absolute;right:35px;top:320px;text-align:right;color:var(--white);font-weight:700;font-size:45px;line-height:62px}

  .intro{position:absolute;left:0;top:581px;width:322px;height:421px;background:var(--white);padding:24px 22px 0 23px;font-weight:300;font-size:17.5px;line-height:23.5px;color:#111}
  .intro p{text-align:justify;margin-bottom:9px}
  .intro p.last{text-align:left}
  .divider{position:absolute;left:322px;top:581px;width:7px;height:421px;background:var(--divider)}
  .facts{position:absolute;left:329px;top:581px;width:447px;height:421px;background:var(--panel-grey)}
  .fact-group{position:absolute;left:18px;width:411px}
  .fact-group.g1{top:55px}
  .fact-group.g2{top:248px}
  .fact{display:flex;justify-content:space-between;align-items:center;height:30px}
  .fact-label{font-weight:700;font-size:22px}
  .fact-value{width:196px;height:30px;border-top:1px solid var(--red-line);border-right:1px solid var(--red-line);text-align:right;padding-right:5px;font-weight:400;font-size:18px;line-height:29px}
  .fact:last-child .fact-value{border-bottom:1px solid var(--red-line)}
  .g2 .fact-value{border-left:1px solid var(--red-line)}

  .agent-bar{position:absolute;left:0;top:1002px;width:322px;height:95px;background:var(--footer-dark);color:var(--white)}
  .agent-name{position:absolute;left:35px;top:17px;font-weight:700;font-size:27px;line-height:25px}
  .agent-rule{position:absolute;left:126px;top:18px;width:2px;height:53px;background:var(--white)}
  .agent-mail{position:absolute;left:137px;top:16px;font-weight:700;font-size:15px}
  .agent-phone{position:absolute;left:137px;top:38px;font-weight:700;font-size:29px;line-height:32px}
  .company-bar{position:absolute;left:329px;top:1002px;width:447px;height:95px;background:var(--footer-grey);color:var(--white);font-weight:700;font-size:19.5px;line-height:26px}
  .company-legal{position:absolute;left:18px;top:19px}
  .company-rule{position:absolute;left:235px;top:20px;width:2px;height:52px;background:var(--white)}
  .company-web{position:absolute;left:248px;top:19px}
</style>
</head>
<body>
  <main class="sheet">
    <section class="hero">
      <div class="hero-photo" role="img" aria-label="Photo du séjour lumineux avec parquet et cuisine ouverte"></div>
      <svg class="hero-accent" width="776" height="581" viewBox="0 0 776 581">
        <polygon points="531,0 776,0 776,581 326,581" fill="var(--red)" opacity="0.93"/>
      </svg>
      <div class="brand">veloranCASA</div>
      <div class="tagline">Spécialiste Romand De Vente Immobilière</div>
      <h1 class="headline">Lumineux<br>4.5 de 100m2<br>idéalement situé<br>1200 Genève</h1>
    </section>

    <section class="intro">
      <p>Professionnels de l’immobilier, nous avons créé la société Veloran Casa Sàrl en 2006 pour répondre aux attentes spécifiques de notre clientèle romande, nationale et internationale.</p>
      <p>Notre volonté est claire : être VOTRE spécialiste romand du courtage immobilier.</p>
      <p>Pour ceci, chaque courtier réside dans sa région d’action et saura vous conseiller au mieux pour la réalisation de votre projet d’achat ou de vente.</p>
      <p class="last">N’hésitez pas à nous contacter !!!!</p>
    </section>
    <div class="divider"></div>
    <section class="facts">
      <div class="fact-group g1">
        <div class="fact"><span class="fact-label">Type de bien</span><span class="fact-value">Appartement</span></div>
        <div class="fact"><span class="fact-label">Surface habitable</span><span class="fact-value">100m2</span></div>
        <div class="fact"><span class="fact-label">Pièces</span><span class="fact-value">4.5</span></div>
        <div class="fact"><span class="fact-label">Surface parcelle</span><span class="fact-value">1’000m2</span></div>
      </div>
      <div class="fact-group g2">
        <div class="fact"><span class="fact-label">Prix</span><span class="fact-value">CHF 910’000.-</span></div>
        <div class="fact"><span class="fact-label">Année</span><span class="fact-value">1994</span></div>
        <div class="fact"><span class="fact-label">Etat</span><span class="fact-value">bon état</span></div>
        <div class="fact"><span class="fact-label">Disponible</span><span class="fact-value">à convenir</span></div>
      </div>
    </section>

    <footer>
      <div class="agent-bar">
        <div class="agent-name">NADIA<br>BERSET</div>
        <div class="agent-rule"></div>
        <div class="agent-mail">berset@velorancasa.ch</div>
        <div class="agent-phone">079 555 18 42</div>
      </div>
      <div class="company-bar">
        <div class="company-legal">Veloran Casa Sàrl<br>1804 Corsier</div>
        <div class="company-rule"></div>
        <div class="company-web">Web: www.velorancasa.ch<br>Tél: 021 555 47 80</div>
      </div>
    </footer>
  </main>
</body>
</html>
```